Business Card Design Project for Architecture and Interior Design company

We need a business card design and logo for an architecture and design firm located in Santiago de Chile. It´s a small company, and the name is "Vostiq" ("Vost" from my surname Vostani, and "arq" for arquitectura or architecture. But it would also be nice that the logo comunicates de Word game "Vosta" as beautiful in italian, and "arq" as architecture".
The idea is to give a delicate, elegant and sofisticated, yet fresh image. Would prefer grey black and white colors, but wouldn´t mind to use another additional color.
I allready have a web page www.vostiq.cl, but would like to improve the logo design.
Please contact if any further information is requiered.
Reason: Need a more arquitectural and desing spirit in the cards. Few of them give that idea.

```html
<!DOCTYPE html>
<html lang="es">
<head>
<meta charset="utf-8">
<title>Vostiq – Tarjetas de presentación</title>
<link rel="stylesheet" href="https://fonts.googleapis.com/css2?family=Nunito+Sans:wght@800&display=swap">
<style>
  :root {
    --card-black: #231f20;
    --band-grey: #999999;
    --paper: #ffffff;
    --ink-light: #ffffff;
  }
  * { margin: 0; padding: 0; box-sizing: border-box; }
  html, body {
    width: 965px;
    height: 1200px;
    overflow: hidden;
    background: var(--paper);
  }
  .sheet {
    position: relative;
    width: 965px;
    height: 1200px;
    font-family: "Nunito Sans", Verdana, sans-serif;
    font-weight: 800;
    color: var(--ink-light);
  }
  .card {
    position: absolute;
    left: 0;
    width: 965px;
    height: 502px;
    background: var(--card-black);
  }
  .card--front { top: 0; }
  .card--back  { top: 666px; height: 503px; }
  .card-band {
    position: absolute;
    left: 0;
    width: 965px;
    height: 24px;
    background: var(--band-grey);
  }
  .card-band--front { top: 508px; }
  .card-band--back  { top: 1175px; }
  .holder-name {
    position: absolute;
    left: 56px;
    top: 96px;
    font-size: 40px;
    line-height: 1;
    letter-spacing: 0.2px;
  }
  .contact {
    position: absolute;
    left: 56px;
    top: 383px;
    font-size: 22px;
    line-height: 28px;
  }
  .wordmark {
    position: absolute;
    left: 562px;
    top: 352px;
    font-size: 94px;
    line-height: 1;
    letter-spacing: 1px;
  }
</style>
</head>
<body>
  <main class="sheet">
    <section class="card card--front">
      <p class="holder-name">Mirela Vostani</p>
      <address class="contact" style="font-style:normal">
        Contacto: info@vostiq.cl<br>
        Fono: +56 9 41235870<br>
        www.vostiq.cl
      </address>
      <p class="wordmark">Vostiq</p>
    </section>
    <div class="card-band card-band--front"></div>

    <section class="card card--back">
      <p class="holder-name">Mirela Vostani</p>
      <address class="contact" style="font-style:normal">
        Contacto: info@vostiq.cl<br>
        Fono: +56 9 41235870<br>
        www.vostiq.cl
      </address>
      <p class="wordmark">Vostiq</p>
    </section>
    <div class="card-band card-band--back"></div>
  </main>
</body>
</html>
```